A new website for Electrical Contractor Business

We are looking for a unique and new WordPress website design which would include 5 Pages - Home Page, Meet the Team, Our Services, Our Projects and Contact Us page.

The global theme for the website needs to be professional but simple to navigate as we cater for both business and home owner customers.

Our core business service is targeted around lighting from single room decorative to large office so the theme should incorporate this in some way.

The home page should include;
Our business logo, Contact number, Email address, small Image rotation box - Highlighting pervious projectsText box - With welcome message, chirpnet feed news reel/Customer feed back box.

I would also like to see a 2 boxes for the separate customer types we services. Business and Home Owner. each box will have a small image with a small text description with a link to the area of the services page relevant to that customer type.

Meet the team page -This will be introducing potential customers to the team so I would like it to include for each team member. Something like a small image and text area which will introduce an outline of the team members skills and abilities.

Our Services page This page will be outlining the different services on offer to the both customer types business and homeowner. Each service should have an image with text description of the service would good here.

Our projects page-Will include images of pervious projects and work we have completed along with a text area for the project description/ outliner.

Contact Us page - Should include a contact form which should include an option for the customer to quest us to call them back, also a selection box for them to inform us our how they found our details would be good.

Colour - The theme colours can be taken from the logo or feel free to impress with your own imagination.

Remember we are looking for a website that will interest our customers enough to except our services or be drawn further into the website.. So call to action links to other areas of the site/ contact page are welcome

Target Market(s)

Business - Office, warehousing and Large Store - lighting and Power
Home owner lighting and power

Coding

Coded - Design and coding required

Number of Pages Required

5+ page

Font styles to use
Serif
Sans Serif

Colors

Designer to choose colors to be used in the design.

Requirements
Must have
• Logo integrated into the website design - i.e. website colours which allow the logo to blend into the design.
Nice to have
• Custom but professional theme catering to business customers, but also show that we do provide services to home owners too.
Should not have
• Sorry am not interested in one oversized block image on rotation covering half the home page.. Images will be needed but not a single block over sized frame with not text, shape. Please use your imagination when considering this design

```html
<!DOCTYPE html>
<html lang="en">
<head>
<meta charset="utf-8">
<title>Lumenwise Electric — Home</title>
<link rel="stylesheet" href="https://fonts.googleapis.com/css2?family=Roboto+Condensed:wght@400;700&family=Roboto:wght@400;500;700&display=swap">
<style>
:root{
  --navy:#1c3166;
  --navy-dark:#18295a;
  --orange:#ef6a25;
  --text:#4a4a4a;
  --muted:#777;
  --white:#fff;
  --light:#f2f2f2;
}
*{margin:0;padding:0;box-sizing:border-box}
html,body{width:1200px;height:3737px;overflow:hidden}
body{font-family:"Roboto",Arial,sans-serif;color:var(--text);background:var(--white);position:relative}
.abs{position:absolute}
.head{font-family:"Roboto Condensed","Arial Narrow",sans-serif;font-weight:700;color:var(--navy);text-transform:uppercase;letter-spacing:.5px}

/* hero */
.hero{position:absolute;left:0;top:0;width:1200px;height:763px;background:linear-gradient(100deg,#7f7d79 0%,#8b8883 35%,#a88f5c 58%,#d99a2e 66%,#8a6a3a 80%,#706a62 100%)}
.navbar{position:absolute;left:89px;top:33px;width:1022px;height:64px;background:var(--white);display:flex;align-items:center;padding:0 35px 0 22px}
.brand{display:flex;align-items:center;gap:10px;font-family:"Roboto",sans-serif;font-weight:500;font-size:17px;color:var(--navy);letter-spacing:.5px;white-space:nowrap}
.brand-dot{width:30px;height:30px;border-radius:50%;background:var(--orange)}
.menu{margin-left:auto;display:flex;gap:33px;font-size:12.5px;font-weight:700;color:#222;text-transform:uppercase;list-style:none}
.menu .active{color:var(--orange)}
.hero-title{position:absolute;left:89px;top:352px;color:var(--white);font-family:"Roboto Condensed",sans-serif;font-weight:700;line-height:1}
.hero-title .l1{font-size:44px;letter-spacing:1px}
.hero-title .l2{font-size:82px;letter-spacing:2px;margin-top:-2px}
.hero-title .l3{font-size:47px;letter-spacing:1px;margin-top:-2px}
.slide-dots{position:absolute;right:40px;top:396px;color:var(--white);font-size:12px;font-weight:700;text-align:right;line-height:23px}
.slide-dots span{display:inline-block;width:9px;height:9px;border-radius:50%;background:var(--white);margin-left:8px}
.slide-dots .faint{opacity:.3;color:var(--orange)}
.slide-dots .faint span{background:var(--orange)}
.scroll-down{position:absolute;left:579px;top:678px}

/* welcome */
.welcome-main{left:132px;top:852px;width:359px;height:444px;background:linear-gradient(160deg,#cfd4d6,#e8e9e6 45%,#6d6560 85%);box-shadow:0 25px 40px rgba(0,0,0,.15)}
.welcome-small{left:377px;top:1114px;width:154px;height:209px;background:linear-gradient(180deg,#b9bcbd,#eceae6 60%,#c8c6c1)}
.welcome-text{left:615px;top:984px;width:470px}
.welcome-text h2{font-size:35px;line-height:34px}
.welcome-text p{margin-top:18px;font-size:14px;line-height:25px;color:var(--text)}
.btn{display:inline-flex;align-items:center;font-family:"Roboto",sans-serif;font-weight:700;font-size:13px;color:var(--white);text-transform:uppercase;height:36px;padding:0 40px 0 21px;clip-path:polygon(0 0,100% 0,82% 100%,0 100%)}
.btn-orange{background:var(--orange)}
.btn-navy{background:var(--navy)}
.welcome-text .btn{margin-top:19px}

/* customer types */
.type-img{top:1423px;width:499px;height:323px}
.type-rule{top:1746px;width:2px;height:60px;background:var(--orange)}
.type-body{top:1786px;width:360px}
.type-body h3{font-size:28px;line-height:30px}
.type-body p{font-size:14.5px;line-height:22px;margin-top:4px}
.arrow-ring{width:42px;height:42px}

/* projects */
.projects-band{left:0;top:1962px;width:846px;height:471px;background:var(--orange)}
.projects-intro{left:87px;top:2135px;width:380px;color:var(--white)}
.projects-intro h2{font-family:"Roboto Condensed",sans-serif;font-weight:700;font-size:33px}
.projects-intro p{font-size:14.5px;line-height:25px;margin-top:6px}
.projects-intro .btn{margin-top:14px;padding-right:44px}
.proj-card{top:2039px;height:326px;background:var(--white);box-shadow:0 4px 12px rgba(0,0,0,.12)}
.proj-card .ph{height:204px}
.proj-card .txt{padding:22px 30px 0 30px}
.proj-card h4{font-size:16px}
.proj-card p{font-size:12.5px;line-height:18px;color:var(--text);margin-top:4px}

/* news */
.news-title{left:0;top:2530px;width:1200px;text-align:center;font-size:33px}
.news-card{top:2580px;width:330px}
.news-card .ph{height:219px}
.date{position:absolute;left:18px;top:206px;width:60px;height:68px;background:var(--navy);color:var(--white);text-align:center;font-family:"Roboto Condensed",sans-serif;font-weight:700}
.date b{display:block;font-size:30px;line-height:38px;margin-top:4px}
.date i{font-style:normal;font-size:13px;letter-spacing:4px}
.news-card h4{position:absolute;left:97px;top:246px;font-size:20px;white-space:nowrap}
.news-card p{position:absolute;left:97px;top:276px;width:220px;font-size:12.5px;line-height:19px}

/* review */
.review-title{left:174px;top:3035px;font-size:34px;line-height:34px}
.review-photo{left:377px;top:3008px;width:140px;height:140px;border-radius:50%;background:radial-gradient(circle at 50% 40%,#c99a7e,#6b5a4d 70%,#8d8c88)}
.quote-mark{left:560px;top:2992px;font-family:Georgia,serif;font-size:150px;line-height:1;color:#e5e5e5}
.review-text{left:564px;top:3045px;width:500px;font-size:18px;line-height:29px;color:#333}
.review-name{left:564px;top:3145px;font-size:18px;font-weight:500;color:var(--orange)}

/* footer */
.footer{left:0;top:3314px;width:1200px;height:423px;background:var(--navy)}
.footer-brand{left:69px;top:3440px;width:240px;text-align:center;color:var(--white)}
.footer-brand .ring{width:86px;height:86px;border-radius:50%;border:5px solid var(--white);margin:0 auto 20px}
.footer-brand .name{font-size:19px;font-weight:500;letter-spacing:1px;white-space:nowrap}
.fcol{top:3420px;color:var(--white);font-size:14px}
.fcol h5{font-family:"Roboto Condensed",sans-serif;font-weight:700;font-size:16px;letter-spacing:.5px;margin-bottom:14px;text-transform:uppercase}
.fcol li{list-style:none;line-height:31px}
.news-input{margin-top:16px;width:234px;height:35px;background:#2a4078;font-size:12px;line-height:35px;padding-left:18px}
.fcol .btn{margin-top:7px;height:35px;font-size:12.5px;padding-right:44px}
.contact-row{display:flex;align-items:center;gap:7px;font-size:13px;line-height:23px;white-space:nowrap}
.socials{display:flex;gap:8px;margin-top:14px}
.socials span{width:25px;height:25px;border-radius:50%}
.footer-rule{left:89px;top:3681px;width:1022px;height:1px;background:#34498a}
.to-top{left:1125px;top:3663px;width:36px;height:36px;border-radius:50%;background:var(--orange)}
.copyright{left:0;top:3703px;width:1200px;text-align:center;color:var(--white);font-size:14px}
</style>
</head>
<body>

<header class="hero" role="img" aria-label="Warm lit wall lamp with fabric shade on a grey wall">
  <nav class="navbar">
    <div class="brand"><span class="brand-dot"></span>LUMENWISE ELECTRIC</div>
    <ul class="menu">
      <li class="active">Home</li><li>Meet the Team</li><li>Our Services</li><li>Projects</li><li>Contact Us</li>
    </ul>
  </nav>
  <h1 class="hero-title">
    <div class="l1">BRIGHTEN YOUR</div>
    <div class="l2">ENVIROMENT</div>
    <div class="l3">WITH EFFECTIVE COST</div>
  </h1>
  <div class="slide-dots">
    <div class="faint">01<span></span></div>
    <div>02<span></span></div>
    <div>03<span></span></div>
  </div>
  <svg class="scroll-down" width="40" height="40" viewBox="0 0 40 40"><circle cx="20" cy="20" r="18" fill="none" stroke="#fff" stroke-width="2"/><path d="M14 17l6 6 6-6" fill="none" stroke="#fff" stroke-width="2"/></svg>
</header>

<section>
  <div class="abs welcome-main" role="img" aria-label="Bright living room with pendant lamp and round coffee table"></div>
  <div class="abs welcome-small" role="img" aria-label="White pendant lamp shade close-up"></div>
  <div class="abs welcome-text">
    <h2 class="head">Welcome to our<br>Lumenwise Electric</h2>
    <p>Lorem Ipsum is simply dummy text of the printing and typesetting industry. Lorem Ipsum has been the industry's standard dummy text ever since the 1500s, when an unknown printer took a galley of type and scrambled it to make a type specimen book.</p>
    <span class="btn btn-orange">Read More</span>
  </div>
</section>

<section>
  <div class="abs type-img" style="left:89px;background:linear-gradient(180deg,#6f6c68,#9a958f 50%,#c9c6c1)" role="img" aria-label="Modern office interior with glass partitions and pendant light"></div>
  <div class="abs type-rule" style="left:108px"></div>
  <div class="abs type-body" style="left:134px">
    <h3 class="head">Customer Type Business</h3>
    <p>Lorem Ipsum is simply dummy text of the printing typesetting industry lorem Ipsum ..</p>
  </div>
  <svg class="abs arrow-ring" style="left:500px;top:1807px" viewBox="0 0 42 42"><circle cx="21" cy="21" r="19" fill="none" stroke="#ef6a25" stroke-width="2"/><path d="M18 15l6 6-6 6" fill="none" stroke="#ef6a25" stroke-width="2"/></svg>

  <div class="abs type-img" style="left:612px;background:linear-gradient(180deg,#8f9296,#b2b4b6 50%,#dcdcda)" role="img" aria-label="Bedroom with bedside lamp and cushions"></div>
  <div class="abs type-rule" style="left:632px"></div>
  <div class="abs type-body" style="left:656px">
    <h3 class="head">Home Owner</h3>
    <p>Lorem Ipsum is simply dummy text of the printing typesetting industry lorem Ipsum ..</p>
  </div>
  <svg class="abs arrow-ring" style="left:1027px;top:1807px" viewBox="0 0 42 42"><circle cx="21" cy="21" r="19" fill="none" stroke="#ef6a25" stroke-width="2"/><path d="M18 15l6 6-6 6" fill="none" stroke="#ef6a25" stroke-width="2"/></svg>
</section>

<section>
  <div class="abs projects-band"></div>
  <div class="abs projects-intro">
    <h2>PROJECTS</h2>
    <p>Lorem Ipsum is simply dummy text of the printing and typesetting industry. Lorem Ipsum has been the industry's standard dummy text ever since .</p>
    <span class="btn btn-navy">View More</span>
  </div>
  <svg class="abs" style="left:243px;top:2268px" width="40" height="40" viewBox="0 0 40 40"><circle cx="20" cy="20" r="18" fill="none" stroke="#fff" stroke-width="2"/><path d="M22 15l-5 5 5 5" fill="none" stroke="#fff" stroke-width="1.8"/></svg>
  <svg class="abs" style="left:288px;top:2268px" width="40" height="40" viewBox="0 0 40 40"><circle cx="20" cy="20" r="18" fill="#f3894f"/><path d="M18 15l5 5-5 5" fill="none" stroke="#fff" stroke-width="1.8"/></svg>

  <div class="abs proj-card" style="left:521px;width:223px">
    <div class="ph" style="background:linear-gradient(180deg,#3b3a3a,#7b6a5a 50%,#a9a39b)" role="img" aria-label="Dining area with pendant lights"></div>
    <div class="txt"><h4 class="head">Projects</h4><p>Lorem Ipsum is simply dummy text of the printing and typesetting .</p></div>
  </div>
  <div class="abs proj-card" style="left:759px;width:223px">
    <div class="ph" style="background:radial-gradient(circle at 50% 55%,#d98a35,#5a2a18 60%,#2a1510)" role="img" aria-label="Cluster of hanging filament bulbs"></div>
    <div class="txt"><h4 class="head">Projects</h4><p>Lorem Ipsum is simply dummy text of the printing and typesetting .</p></div>
  </div>
  <div class="abs proj-card" style="left:998px;width:230px">
    <div class="ph" style="background:linear-gradient(180deg,#2a2622,#b08a5a 40%,#4a3e32)" role="img" aria-label="Tripod floor lamp with drum shade"></div>
    <div class="txt"><h4 class="head">Projects</h4><p>Lorem Ipsum is simply dummy text of the printing and typesetting .</p></div>
  </div>
</section>

<section>
  <h2 class="abs head news-title">Latest News</h2>
  <article class="abs news-card" style="left:89px">
    <div class="ph" style="background:radial-gradient(circle at 45% 55%,#e0953a,#7a4a2a 55%,#5a3a2a)" role="img" aria-label="Caged filament pendant bulb"></div>
    <div class="date"><b>09</b><i>NOV</i></div>
    <h4 class="head">News Heading Here</h4>
    <p>Lorem Ipsum is simply dummy text of the printing and typesetting industry lorem Ipsum has .</p>
  </article>
  <article class="abs news-card" style="left:435px">
    <div class="ph" style="background:linear-gradient(180deg,#e6e6e6,#d6d6d6)" role="img" aria-label="Copper geometric pendant light"></div>
    <div class="date" style="background:var(--orange)"><b>09</b><i>NOV</i></div>
    <h4 class="head">News Heading Here</h4>
    <p>Lorem Ipsum is simply dummy text of the printing and typesetting industry lorem Ipsum has .</p>
  </article>
  <article class="abs news-card" style="left:781px">
    <div class="ph" style="background:linear-gradient(180deg,#f1f1f1,#c9c9c9 60%,#7d7d7d)" role="img" aria-label="Grey sofa beside a floor lamp"></div>
    <div class="date"><b>09</b><i>NOV</i></div>
    <h4 class="head">News Heading Here</h4>
    <p>Lorem Ipsum is simply dummy text of the printing and typesetting industry lorem Ipsum has .</p>
  </article>
</section>

<section>
  <h2 class="abs head review-title">Customer<br>Review</h2>
  <div class="abs review-photo" role="img" aria-label="Customer portrait"></div>
  <div class="abs quote-mark">&ldquo;</div>
  <p class="abs review-text">Lorem Ipsum is simply dummy text of the printing and typesetting industry lorem Ipsum has been the industry's standard dummy text ever since .</p>
  <div class="abs review-name">Daniel Hart</div>
  <svg class="abs" style="left:564px;top:3195px" width="40" height="40" viewBox="0 0 40 40"><circle cx="20" cy="20" r="19" fill="#e4e4e4"/><path d="M22 15l-5 5 5 5" fill="none" stroke="#555" stroke-width="1.8"/></svg>
  <svg class="abs" style="left:608px;top:3195px" width="40" height="40" viewBox="0 0 40 40"><circle cx="20" cy="20" r="19" fill="#ef6a25"/><path d="M18 15l5 5-5 5" fill="none" stroke="#fff" stroke-width="1.8"/></svg>
</section>

<footer>
  <div class="abs footer"></div>
  <div class="abs footer-brand"><div class="ring"></div><div class="name">LUMENWISE ELECTRIC</div></div>
  <div class="abs fcol" style="left:393px">
    <h5>Useful Links</h5>
    <ul><li>Home</li><li>Meet the Team</li><li>Our Services</li><li>Projects</li><li>Contact Us</li></ul>
  </div>
  <div class="abs fcol" style="left:636px">
    <h5>Newsletter</h5>
    <div>Subscribe to our newsletter</div>
    <div class="news-input">Email Address</div>
    <span class="btn btn-orange">Subscribe</span>
  </div>
  <div class="abs fcol" style="left:924px">
    <h5>Contact Us</h5>
    <div class="contact-row"><svg width="10" height="12" viewBox="0 0 10 12"><path d="M5 0a4 4 0 0 0-4 4c0 3 4 8 4 8s4-5 4-8a4 4 0 0 0-4-4z" fill="#ef6a25"/></svg>Some goes address here</div>
    <div class="contact-row"><svg width="11" height="11" viewBox="0 0 11 11"><path d="M2 0l2 2.5-1 1.5a7 7 0 0 0 4 4l1.5-1L11 9l-1.5 2C5 11 0 6 0 1.5z" fill="#ef6a25"/></svg>+44 ( 0161 ) 204</div>
    <div class="contact-row"><svg width="11" height="9" viewBox="0 0 11 9"><rect width="11" height="9" fill="#ef6a25"/><path d="M0 0l5.5 5L11 0" fill="none" stroke="#1c3166"/></svg>hello@lumenwise.co</div>
    <div class="socials">
      <span style="background:#3b5ba0" aria-label="friendloop"></span>
      <span style="background:#2aa3e6" aria-label="chirpnet"></span>
      <span style="background:#d6423a" aria-label="circlecast"></span>
    </div>
  </div>
  <div class="abs footer-rule"></div>
  <svg class="abs to-top" viewBox="0 0 36 36"><path d="M13 20l5-5 5 5" fill="none" stroke="#fff" stroke-width="1.8"/></svg>
  <div class="abs copyright">Copyright 2019 | All Right Reserved</div>
</footer>

</body>
</html>
```